Sassy, natural personal lubricant knows that it is not always about the packaging

An opportunity exists to create packaging for the world's first Macadamia Oil personal lubricant - Vorrabee Silk. Unlike any other personal lubricants, this product is created from pure macadamia nut oil. The fatty acids naturally occurring in Macadamia oil are highly anti-inflammatory and are the closest in composition to human skin lipids. Using Vorrabee Silk in such a vulnerable part of our bodies is the safest and gentlest way to enhance sexual enjoyment while moisturizing and adding lubrication. Vorrabee Silk is completely free of the parabens, glycerins, fragrances, hormones, silicones and petroleum products known to irritate the delicate vaginal wall.

Design tone for Vorrabee Silk:
- intelligent, but not condescending or patronizing
- elegant and dignified but not prudish
- clean, natural, uninhibited

Design specs:
- See attached file for packaging specs

Colors:
- refer to www.vorrabee-example.com to see other products in the range. This is a guide only. Use of those colors is not mandatory.

Ingredients:

100% Macadamia Oil

Additional features:

- edible
- vegan
- gluten-free
- low allergen
- naturally anti-microbial and anti-inflammatory

See http://plumfernlab-example.com/benefits-of-macadamia-nut-oil-in-skin-care/ for a list of the benefits of macadamia oil.

Target Market(s)

Our target market are the early adopters within the baby boomer set. Their age is a badge of honor, they are comfortable in their own skin and as sensual and fun-loving as ever. They are in their prime - still cool, still curious, still a little crazy. They are open to new possibilities, just as they have been at every age and stage. They still have plenty to do and plenty to enjoy. Being pre-menopausal or menopausal, natural lubrication may be diminishing. Vorrabee Silk is the completely natural way to bring back the pleasure in sex.

Requirements
Must have
• Brandname: Vorrabee Silk

Container Packaging specs: http://www.gravelpackco-example.com/images/art/7845K16-K-OAK-PRESSED.PDF
Dispenser: http://www.gravelpackco-example.com/lotion-dispenser-pumps/p/kMQ730R/
Should not have
• No post-coital pictures
No people
Nothing phallic

```html
<!DOCTYPE html>
<html lang="en">
<head>
<meta charset="utf-8">
<title>Vorrabee Silk – Macadamia Oil Label</title>
<link rel="stylesheet" href="https://fonts.googleapis.com/css2?family=Oswald:wght@400;500;600&display=swap">
<style>
  :root {
    --bg-top: #5b4330;
    --bg-mid: #7a4f2a;
    --bg-bottom: #b8661c;
    --band-light: #b9d147;
    --band-deep: #6aa843;
    --brown: #4a1c0d;
    --brown-ink: #5a2614;
    --ring: #a7cf3a;
    --nut-light: #d9b688;
    --nut-dark: #8a5530;
    --white: #ffffff;
  }
  * { margin: 0; padding: 0; box-sizing: border-box; }
  html, body { width: 1200px; height: 951px; overflow: hidden; background: #fff; }
  .label {
    position: relative;
    width: 1200px;
    height: 951px;
    overflow: hidden;
    font-family: "Oswald", "Arial Narrow", sans-serif;
  }
  .label__pattern {
    position: absolute; inset: 0;
    background:
      radial-gradient(ellipse at 18% 30%, rgba(255,220,160,0.10), transparent 55%),
      radial-gradient(ellipse at 82% 30%, rgba(255,220,160,0.10), transparent 55%),
      linear-gradient(180deg, var(--bg-top) 0%, var(--bg-mid) 50%, var(--bg-bottom) 100%);
  }
  .label__band {
    position: absolute;
    left: 398px; top: 0;
    width: 410px; height: 951px;
    background: linear-gradient(180deg,
      var(--band-light) 0%, var(--band-light) 22%,
      var(--band-deep) 36%, var(--band-deep) 62%,
      var(--band-light) 80%, var(--band-light) 100%);
  }
  .brand {
    position: absolute;
    left: 398px; top: 40px; width: 410px;
    display: flex; flex-direction: column; align-items: center;
  }
  .brand__dot {
    width: 150px; height: 150px; border-radius: 50%;
    background: var(--brown-ink);
  }
  .brand__name {
    margin-top: 14px;
    font-size: 60px; font-weight: 500; line-height: 1;
    color: var(--brown-ink);
    letter-spacing: 1px;
  }
  .title-oval {
    position: absolute;
    left: 226px; top: 330px;
  }
  .product-name {
    position: absolute;
    left: 0; width: 1200px; top: 408px;
    text-align: center;
    font-size: 84px; font-weight: 500; line-height: 1;
    color: var(--white);
    letter-spacing: 1px;
    text-shadow: 0 4px 6px rgba(0,0,0,0.45);
  }
  .nuts {
    position: absolute;
    left: 438px; top: 526px;
    width: 292px; height: 150px;
    border-radius: 70px;
    background: radial-gradient(ellipse at 50% 50%, var(--nut-light) 0%, var(--nut-dark) 70%, rgba(138,85,48,0) 100%);
  }
  .ingredient {
    position: absolute;
    left: 398px; width: 410px; top: 705px;
    text-align: center;
    font-size: 39px; font-weight: 500; line-height: 1;
    color: var(--white);
  }
  .features {
    position: absolute;
    left: 398px; width: 410px; top: 762px;
    list-style: none;
    text-align: center;
    color: var(--white);
    font-size: 22px; font-weight: 400; line-height: 27.5px;
  }
</style>
</head>
<body>
  <main class="label">
    <div class="label__pattern" role="img" aria-label="Ornate paisley and floral lace pattern in warm browns"></div>
    <div class="label__band"></div>

    <header class="brand">
      <span class="brand__dot"></span>
      <span class="brand__name">vorrabee</span>
    </header>

    <svg class="title-oval" width="748" height="300" viewBox="0 0 748 300" aria-hidden="true">
      <ellipse cx="374" cy="150" rx="364" ry="142" fill="var(--brown)" stroke="var(--ring)" stroke-width="5"/>
    </svg>

    <h1 class="product-name">VORRABEE SILK</h1>

    <div class="nuts" role="img" aria-label="Photograph of whole and cracked macadamia nuts"></div>

    <p class="ingredient">100% MACADAMIA OIL</p>

    <ul class="features">
      <li>EDIBLE</li>
      <li>VEGAN</li>
      <li>GLUTEN-FREE</li>
      <li>LOW ALLERGEN</li>
      <li>NATURALLY ANTI-MICROBIAL</li>
      <li>ANTI-INFLAMMATORY</li>
    </ul>
  </main>
</body>
</html>
```